Brenwick Drilling Inc. Business card design

Business card design for "Brenwick Drilling Inc. - Directional Drilling Services"

Address is:

Brenwick Drilling Inc.
512 - 73 Tolvane Crescent SW
Calgary, Alberta, Canada
T2K 4P8

Please incorporate the logo design into the card, thank you.

Target Market(s)

Oil & Gas and Drilling

Industry/Entity Type

Business

```html
<!DOCTYPE html>
<html lang="en">
<head>
<meta charset="utf-8">
<title>Brenwick Drilling Inc. – Business Card</title>
<link rel="stylesheet" href="https://fonts.googleapis.com/css2?family=Montserrat:wght@700&family=Raleway:wght@400;500&display=swap">
<style>
  :root {
    --canvas: #e7e4df;
    --ink: #2b2b2b;
    --black: #141414;
    --black-soft: #262626;
    --red: #e0323f;
    --grey: #9a9a9a;
    --white: #ffffff;
    --light-text: #d6d6d6;
  }
  * { margin: 0; padding: 0; box-sizing: border-box; }
  html, body { width: 1200px; height: 1023px; overflow: hidden; background: var(--canvas); }
  body { position: relative; font-family: "Raleway", sans-serif; }

  .card {
    position: absolute;
    left: 250px;
    width: 700px;
    height: 400px;
    border-radius: 6px;
    overflow: hidden;
    box-shadow: 0 10px 28px rgba(0,0,0,.22);
  }
  .card--front { top: 70px; background: var(--white); }
  .card--back {
    top: 553px;
    background: radial-gradient(circle at 50% 45%, var(--black-soft) 0%, var(--black) 70%);
  }
  .card__art { position: absolute; inset: 0; }

  .brand { position: absolute; text-align: center; }
  .brand__mark {
    display: block;
    margin: 0 auto 12px;
    width: 60px; height: 60px;
    border-radius: 50%;
    border: 4px solid var(--red);
  }
  .brand__name {
    font-family: "Montserrat", sans-serif;
    font-weight: 700;
    font-size: 24px;
    letter-spacing: 1px;
    text-transform: uppercase;
    white-space: nowrap;
  }
  .brand__tagline {
    margin-top: 4px;
    font-size: 10.5px;
    letter-spacing: 4.2px;
    text-transform: uppercase;
    white-space: nowrap;
  }

  .card--front .brand { left: 100px; top: 22px; width: 330px; }
  .card--front .brand__name { color: var(--ink); }
  .card--front .brand__tagline { color: #555; }

  .card--back .brand { left: 185px; top: 120px; width: 330px; }
  .card--back .brand__mark { border-color: var(--white); }
  .card--back .brand__name { color: var(--white); }
  .card--back .brand__tagline { color: var(--light-text); }

  .holder {
    position: absolute; left: 190px; top: 232px;
    font-size: 21px; font-weight: 500; color: var(--red);
  }
  .holder__role { font-size: 17px; }

  .contacts { position: absolute; left: 40px; top: 292px; list-style: none; }
  .contacts li, .address {
    display: flex; align-items: center; gap: 12px;
    color: var(--light-text); font-size: 16px; line-height: 31px;
  }
  .icon { width: 14px; height: 14px; flex: none; }

  .address { position: absolute; left: 410px; top: 200px; align-items: flex-start; line-height: 24px; }
  .address .icon { width: 22px; height: 22px; margin-top: 14px; }
</style>
</head>
<body>

  <section class="card card--front" aria-label="Business card front">
    <svg class="card__art" viewBox="0 0 700 400" aria-hidden="true">
      <path d="M0 206 C240 196 500 150 700 58" fill="none" stroke="var(--red)" stroke-width="5"/>
      <path d="M0 214 C240 204 500 158 700 66 L700 400 L0 400 Z" fill="var(--black)"/>
      <path d="M0 220 C240 210 500 164 700 72" fill="none" stroke="var(--grey)" stroke-width="2" opacity=".7"/>
    </svg>

    <div class="brand">
      <span class="brand__mark"></span>
      <p class="brand__name">Brenwick Drilling Inc.</p>
      <p class="brand__tagline">Directional Drilling Services</p>
    </div>

    <p class="holder">Daniel Reyes <span class="holder__role">| Director</span></p>

    <address class="address">
      <svg class="icon" viewBox="0 0 24 24" aria-hidden="true"><circle cx="12" cy="12" r="12" fill="var(--red)"/><path d="M12 5a4.5 4.5 0 0 0-4.5 4.5C7.5 13 12 19 12 19s4.5-6 4.5-9.5A4.5 4.5 0 0 0 12 5zm0 6.2a1.7 1.7 0 1 1 0-3.4 1.7 1.7 0 0 1 0 3.4z" fill="var(--black)"/></svg>
      <span>512 - 73 Tolvane Crescent SW<br>Calgary, Alberta, Canada<br>T2K 4P8</span>
    </address>

    <ul class="contacts">
      <li><svg class="icon" viewBox="0 0 14 14" aria-hidden="true"><circle cx="7" cy="7" r="7" fill="var(--red)"/><path d="M4.5 3.5l1.3 0 .6 1.6-.8.6c.4.9 1 1.5 1.9 1.9l.6-.8 1.6.6v1.3c-3 .2-5.4-2.2-5.2-5.2z" fill="var(--black)"/></svg>4183 2956</li>
      <li><svg class="icon" viewBox="0 0 14 14" aria-hidden="true"><circle cx="7" cy="7" r="7" fill="var(--red)"/><rect x="3.5" y="4.5" width="7" height="5" fill="none" stroke="var(--black)" stroke-width="1"/><path d="M3.5 4.5l3.5 3 3.5-3" fill="none" stroke="var(--black)" stroke-width="1"/></svg>info@brenwickdrilling.com</li>
      <li><svg class="icon" viewBox="0 0 14 14" aria-hidden="true"><circle cx="7" cy="7" r="7" fill="var(--red)"/><circle cx="7" cy="7" r="3.5" fill="none" stroke="var(--black)" stroke-width="1"/><path d="M3.5 7h7M7 3.5v7" stroke="var(--black)" stroke-width="1"/></svg>www.BrenwickDrilling.com</li>
    </ul>
  </section>

  <section class="card card--back" aria-label="Business card back">
    <svg class="card__art" viewBox="0 0 700 400" aria-hidden="true">
      <circle cx="350" cy="190" r="175" fill="none" stroke="#ffffff" stroke-opacity=".05" stroke-width="22"/>
      <circle cx="350" cy="190" r="260" fill="none" stroke="#ffffff" stroke-opacity=".035" stroke-width="16"/>
    </svg>
    <div class="brand">
      <span class="brand__mark"></span>
      <p class="brand__name">Brenwick Drilling Inc.</p>
      <p class="brand__tagline">Directional Drilling Services</p>
    </div>
  </section>

</body>
</html>
```